Business card design needed

This is a roofing company that specialises in metal roofs on period homes. I want to market to the more affluent areas in Melbourne as they are very expensive homes and period style. If you look at period homes in Melbourne you will see the metal roofs with ornate guttering and lattice work. An image of a roof or part of it would look good on the card - as it will catch the eye of the home owner in my view.

I dont have a logo so feel free to do what you want. I am open to all ideas and will choose the most appropriate.

I want to make the card look very professional and upmarket. Most roofers just use cards made cheaply, so this is my opportunity to differentiate from those. I dont want a cheap looking card. Must really look professional and make the home owner think I am very good at what I do.

I am going to put these cards in letter boxes to market my business. As this has worked before.

A good example of period homes with the roofs I work on are:
http://www.brindleford-estates.com.au/Brindleford-Estates-photo-gallery.html
Please check out the houses in the gallery. If I can get the message across with a beautiful photo of a roof - the home owner will be enticed to call me based on the image. I believe the image of the period home roof - or part of - will make a difference. As most of my competitors just have a sketch or words.

I will be making a quality card that is thick and printed in high resolution.
Updates

Target Market(s)

Home owners who are most likely tertiary educated and high income earners.

Industry/Entity Type

Roofing

Contact Information for Business Card

Mr Dean Ollivant
Professional Roofing Expert (est 30 years)
No obligation appraisal
Licensed. Quality. Guaranteed.

Mobile: 0438 726 091
Fax: 9837 2450
Email: toptilecraft.vic@mailbox-example.com

On the back of the card can you put.....
Metal Roofing Specialists
Quality Period Home Experience
New and Old Roofing Expertise
Roof Maintenance and Repair
Over 30 years experience
References Provided
Polite and Punctual

Requirements
Nice to have
• I am open to all ideas. Layout and design is up to you. Go for it.

```html
<!DOCTYPE html>
<html lang="en">
<head>
<meta charset="utf-8">
<title>Roofing Expert Business Card</title>
<link rel="stylesheet" href="https://fonts.googleapis.com/css2?family=Roboto+Condensed:wght@400;700;900&display=swap">
<style>
  :root {
    --page-bg: #e9eaec;
    --roof-dark: #3b3d4c;
    --roof-mid: #555869;
    --roof-deep: #2c2e3a;
    --trim-white: #c9cacf;
    --trim-shade: #8c8f9c;
    --card-text: #ffffff;
    --text-shadow: rgba(0, 0, 0, 0.75);
  }
  * { margin: 0; padding: 0; box-sizing: border-box; }
  html, body {
    width: 1200px;
    height: 861px;
    overflow: hidden;
    background: var(--page-bg);
  }
  .canvas {
    position: relative;
    width: 1200px;
    height: 861px;
  }
  .card {
    position: absolute;
    top: 265px;
    width: 540px;
    height: 330px;
    overflow: hidden;
    box-shadow: 0 6px 18px rgba(0, 0, 0, 0.25);
  }
  .card--front { left: 40px; }
  .card--back { left: 620px; }
  .card__photo {
    position: absolute;
    inset: 0;
    background:
      linear-gradient(135deg, transparent 88%, var(--trim-white) 88%, var(--trim-shade) 100%),
      linear-gradient(225deg, transparent 10%, var(--trim-white) 10%, var(--trim-shade) 15%, transparent 15%),
      linear-gradient(200deg, var(--roof-mid) 0%, var(--roof-dark) 55%, var(--roof-deep) 100%);
  }
  .card__content {
    position: absolute;
    left: 34px;
    top: 88px;
    transform: rotate(-13deg);
    transform-origin: left top;
    color: var(--card-text);
    font-family: "Roboto Condensed", Arial, sans-serif;
    text-shadow: 2px 2px 2px var(--text-shadow);
    white-space: nowrap;
  }
  .owner-name {
    font-weight: 900;
    font-size: 36px;
    line-height: 1.05;
  }
  .owner-title {
    font-weight: 400;
    font-size: 23px;
    margin-bottom: 14px;
  }
  .contact-list {
    list-style: none;
    font-size: 19px;
    line-height: 1.55;
    padding-left: 18px;
  }
  .contact-list li { padding-left: calc(var(--i) * 12px); }
  .card--back .card__content { left: 26px; top: 108px; }
  .tagline {
    font-weight: 900;
    font-size: 19px;
    line-height: 1.1;
    margin-bottom: 6px;
    text-transform: uppercase;
  }
  .service-list {
    list-style: none;
    font-weight: 700;
    font-size: 16px;
    line-height: 1.4;
    padding-left: 30px;
  }
  .service-list li { padding-left: calc(var(--i) * 9px); }
  .service-list li::before { content: "\2022\00a0"; }
</style>
</head>
<body>
<main class="canvas">
  <section class="card card--front" aria-label="Business card front">
    <div class="card__photo" role="img" aria-label="Photograph of a slate grey period home roof with white gable trim"></div>
    <div class="card__content">
      <h1 class="owner-name">Mr. Dean Ollivant</h1>
      <p class="owner-title">Professional Roofing Expert</p>
      <ul class="contact-list">
        <li style="--i:0">Mobile: 0438 726 091</li>
        <li style="--i:1">Fax: 9837 2450</li>
        <li style="--i:2">Email: toptilecraft.vic@mailbox-example.com</li>
      </ul>
    </div>
  </section>

  <section class="card card--back" aria-label="Business card back">
    <div class="card__photo" role="img" aria-label="Photograph of a slate grey period home roof with white gable trim"></div>
    <div class="card__content">
      <p class="tagline">No obligation appraisal &bull; Licensed<br>Quality &bull; Guaranteed</p>
      <ul class="service-list">
        <li style="--i:0">Metal Roofing Specialists</li>
        <li style="--i:1">Quality Period Home Experience</li>
        <li style="--i:2">New and Old Roofing Expertise</li>
        <li style="--i:3">Roof Maintenance and Repair</li>
        <li style="--i:4">Over 30 years experience</li>
        <li style="--i:5">References Provided</li>
        <li style="--i:6">Polite and Punctual</li>
      </ul>
    </div>
  </section>
</main>
</body>
</html>
```